Birchby Candles, Hand-poured scented soy candles

Create a logo and label design to use on my vintage country farmhouse style, all natural, hand poured soy candle jars and apothecaries. Candles will be labeled in 4 different sizes so design must be adaptable, clean, simple, telegraphic and invoke interest in the product. Think Black lettering on white or black on kraft brown. 603 is the area code for New Hampshire where we make them. The labels will need a prominent area for the scent of the candle to be listed that the eyes are drawn to. Primitive country in design? Use of state attractions? Jars are a square mason style 8 ounce and 16 ounce. Tarts are a clamshell. Lids are a 70-400 series 2.5" label area. Candles are white in a clear glass jar, black lids. There will be label design sizes of 3"x 2.5" 2.5" round, 1.5"x2.5"

Target Market(s)

primitive country, farmhouse, vintage, general home decor

Contact Information for Business Card

Birchby Candles, all natural soy candles, hand-poured in New Hampshire, logo, phone, address. Possibly match the main label.

Logo Text

Birchby Candles, all natural soy candles, hand-poured in New Hampshire, area for scent description and size of container.

Font styles to use
Serif
Script

Colors

Designer to choose colors to be used in the design.

Requirements
Must have
• simple and clean, country farmhouse with a bit of vintage thrown in. possibly multiple fonts to distinguish info from scent name
Nice to have
• at this time I am open to suggestions
• Prefer scent names or brand name in an older script?
• older copperplate/Spencerian?
Should not have
• cluttered, busy, too modern, multiple colors

```html
<!DOCTYPE html>
<html lang="en">
<head>
<meta charset="utf-8">
<title>Birchby Candles – Scent Labels</title>
<link href="https://fonts.googleapis.com/css2?family=Great+Vibes&family=Montserrat:wght@600;700&display=swap" rel="stylesheet">
<style>
  :root {
    --ink: #111111;
    --paper: #ffffff;
    --panel: rgba(255,255,255,0.86);
    --pattern: #d4d4d4;
    --stage-top: #ffffff;
    --stage-bottom: #d6d6d6;
  }
  * { margin: 0; padding: 0; box-sizing: border-box; }
  html, body { width: 1200px; height: 2207px; overflow: hidden; background: var(--paper); }
  .sheet { position: relative; width: 1200px; height: 2207px; overflow: hidden; background: var(--paper); }
  .stage {
    position: absolute; left: 0; top: 0; width: 1200px; height: 1230px;
    background: linear-gradient(180deg, var(--stage-top) 0%, var(--stage-bottom) 100%);
  }
  .label { position: absolute; font-family: "Montserrat", Arial, sans-serif; color: var(--ink); text-align: center; }
  .floral-pattern { position: absolute; inset: 0; background: var(--pattern); }
  .label--round .floral-pattern { border-radius: 50%; }
  .panel { position: absolute; background: var(--panel); }
  .label--round .panel { border-radius: 50%; }
  .content { position: absolute; left: 0; right: 0; display: flex; flex-direction: column; align-items: center; }
  .scent { font-family: "Great Vibes", cursive; font-weight: 400; line-height: 1; color: var(--ink); }
  .size { font-weight: 700; }
  .band {
    background: var(--ink); color: var(--paper); font-weight: 700; text-transform: uppercase;
    white-space: nowrap; line-height: 1; width: auto;
    box-shadow: inset 0 3px 0 var(--ink), inset 0 4px 0 var(--paper),
                inset 0 -3px 0 var(--ink), inset 0 -4px 0 var(--paper);
    position: relative;
  }
  .band::before, .band::after {
    content: ""; position: absolute; left: -6px; right: -6px; height: 2px; background: var(--ink);
  }
  .band::before { top: 0; }
  .band::after { bottom: 0; }
  .tagline { font-weight: 600; text-transform: uppercase; line-height: 1.3; }

  /* small rectangular label */
  .label--small { left: 239px; top: 72px; width: 262px; height: 436px; }
  .label--small .panel { left: 28px; top: 58px; width: 210px; height: 350px; }
  .label--small .content { top: 118px; }
  .label--small .scent { font-size: 62px; }
  .label--small .size { font-size: 15px; margin-top: 22px; }
  .label--small .band { font-size: 12px; letter-spacing: 1.6px; padding: 5px 10px 5px 11.6px; margin-top: 30px; }
  .label--small .tagline { font-size: 12.5px; letter-spacing: 2.5px; margin-top: 12px; line-height: 1.35; }

  /* round label */
  .label--round { left: 532px; top: 72px; width: 436px; height: 436px; }
  .label--round .panel { left: 40px; top: 36px; width: 356px; height: 356px; }
  .label--round .content { top: 140px; }
  .label--round .scent { font-size: 84px; }
  .label--round .band { font-size: 15px; letter-spacing: 3px; padding: 5px 14px 5px 17px; margin-top: 22px; }
  .label--round .tagline { font-size: 12px; letter-spacing: 1.5px; margin-top: 8px; line-height: 1.25; }

  /* large label */
  .label--large { left: 241px; top: 556px; width: 723px; height: 602px; }
  .label--large .panel { left: 58px; top: 59px; width: 608px; height: 485px; }
  .label--large .content { top: 165px; }
  .label--large .scent { font-size: 128px; }
  .label--large .size { font-size: 20px; margin-top: 34px; }
  .label--large .band { font-size: 30px; letter-spacing: 6px; padding: 9px 24px 9px 30px; margin-top: 18px; }
  .label--large .tagline { font-size: 18.5px; letter-spacing: 3px; margin-top: 14px; line-height: 1.28; }
</style>
</head>
<body>
<main class="sheet">
  <div class="stage"></div>

  <section class="label label--small">
    <div class="floral-pattern" role="img" aria-label="Hand-drawn black and grey wildflower and lavender sprig pattern"></div>
    <div class="panel"></div>
    <div class="content">
      <h2 class="scent">Lavander</h2>
      <p class="size">16 Oz</p>
      <p class="band">Birchby Candles</p>
      <p class="tagline">All natural<br>soy candles<br>hand-poured in<br>New Hampshire</p>
    </div>
  </section>

  <section class="label label--round">
    <div class="floral-pattern" role="img" aria-label="Hand-drawn black and grey wildflower and lavender sprig pattern"></div>
    <div class="panel"></div>
    <div class="content">
      <h2 class="scent">Lavander</h2>
      <p class="band">Birchby Candles</p>
      <p class="tagline">All natural soy candles,<br>hand-poured in<br>New Hampshire</p>
    </div>
  </section>

  <section class="label label--large">
    <div class="floral-pattern" role="img" aria-label="Hand-drawn black and grey wildflower and lavender sprig pattern"></div>
    <div class="panel"></div>
    <div class="content">
      <h1 class="scent">Lavander</h1>
      <p class="size">16 Oz</p>
      <p class="band">Birchby Candles</p>
      <p class="tagline">All natural soy candles,<br>hand-poured in New Hampshire</p>
    </div>
  </section>
</main>
</body>
</html>
```